New Plumbing Company

We are looking for a smart and creative business card design for our new plumbing company. We are looking for creativity and originality in our business cards.

Industry/Entity Type

Plumbing

Contact Information for Business Card

Crestline Plumbing
Peter Halvane
Managing Director
Telephone Number : 0481529604
Email : service@crestlineplumbing.com.au
Website : www.crestlineplumbing.com.au
Lic. 508264K

Colors
0692cd
33a6d7
000000

Requirements
Must have
• I want the business card to be designed on a black background using the blue tones i have selected as seen in the company logo.

```html
<!DOCTYPE html>
<html lang="en">
<head>
<meta charset="utf-8">
<title>Crestline Plumbing – Business Card</title>
<link href="https://fonts.googleapis.com/css2?family=Lato:wght@300;400&display=swap" rel="stylesheet">
<style>
  :root {
    --bg: #000000;
    --card-white: #fbfbfb;
    --brand-blue: #0692cd;
    --brand-blue-light: #33a6d7;
    --back-blue: #1b7fc2;
    --ink: #1a1a1a;
    --rule: #3a3a3a;
    --white: #ffffff;
  }
  * { margin: 0; padding: 0; box-sizing: border-box; }
  html, body { width: 1200px; height: 1023px; overflow: hidden; }
  body {
    background: var(--bg);
    font-family: "Lato", Arial, sans-serif;
    position: relative;
  }
  .card {
    position: absolute;
    width: 600px;
    height: 366px;
    border-radius: 3px;
    box-shadow: 0 10px 30px rgba(6,146,205,0.18);
    overflow: hidden;
  }

  /* Front */
  .card-front { left: 90px; top: 80px; background: var(--card-white); }
  .card-front .bottom-band {
    position: absolute; left: 0; right: 0; bottom: 0; height: 12px;
    background: var(--brand-blue);
  }
  .card-front .edge-tab {
    position: absolute; left: 0; top: 150px; width: 6px; height: 46px;
    background: var(--brand-blue);
  }
  .front-brand {
    position: absolute; left: 240px; top: 64px;
    display: flex; align-items: center; gap: 12px;
  }
  .brand-dot {
    width: 38px; height: 38px; border-radius: 50%;
    border: 3px solid var(--brand-blue);
    flex: none;
  }
  .brand-name {
    font-weight: 300; font-size: 30px; letter-spacing: 0.5px;
    color: var(--brand-blue); white-space: nowrap;
  }
  .divider {
    position: absolute; left: 205px; top: 182px; width: 360px; height: 1px;
    background: var(--rule);
  }
  .person { position: absolute; left: 36px; top: 150px; }
  .person-name { font-size: 22px; color: var(--ink); font-weight: 400; }
  .person-title { font-size: 15px; color: var(--brand-blue); margin-top: 2px; }
  .address {
    position: absolute; left: 150px; top: 232px;
    font-size: 15px; line-height: 1.3; color: var(--ink);
  }
  .contact {
    position: absolute; right: 30px; top: 206px;
    list-style: none; text-align: right;
    font-size: 15px; line-height: 1.45; color: var(--ink);
  }
  .contact li { display: flex; justify-content: flex-end; align-items: center; gap: 8px; }
  .contact svg { width: 13px; height: 13px; flex: none; }

  /* Back */
  .card-back {
    left: 510px; top: 580px;
    background: linear-gradient(160deg, var(--brand-blue-light) 0%, var(--back-blue) 55%, #1672b0 100%);
    color: var(--white);
  }
  .back-brand {
    position: absolute; left: 0; right: 0; top: 130px;
    display: flex; justify-content: center; align-items: center; gap: 16px;
  }
  .back-brand .brand-dot { border-color: var(--white); width: 44px; height: 44px; }
  .back-brand .brand-name { color: var(--white); font-size: 38px; }
  .licence-row {
    position: absolute; left: 40px; right: 40px; bottom: 44px;
    display: flex; align-items: center; gap: 18px;
  }
  .licence-row .line { flex: 1; height: 1px; background: rgba(255,255,255,0.85); }
  .licence {
    font-size: 15px; letter-spacing: 4px; color: var(--white); font-weight: 300;
  }
</style>
</head>
<body>
  <section class="card card-front" aria-label="Business card front">
    <div class="edge-tab"></div>
    <div class="front-brand">
      <span class="brand-dot"></span>
      <span class="brand-name">Crestline Plumbing</span>
    </div>
    <div class="divider"></div>
    <div class="person">
      <p class="person-name">Peter Halvane</p>
      <p class="person-title">Managing Director</p>
    </div>
    <p class="address">Here your company or<br>home address</p>
    <ul class="contact">
      <li>0481529604
        <svg viewBox="0 0 16 16" aria-hidden="true"><path d="M4 1.5l2.3 3-1.4 1.6a8 8 0 0 0 5 5l1.6-1.4 3 2.3-1.4 2.3C7.8 14.8 1.2 8.2 1.7 2.9z" fill="#0692cd"/></svg>
      </li>
      <li>service@crestlineplumbing.com.au
        <svg viewBox="0 0 16 16" aria-hidden="true"><rect x="1" y="3" width="14" height="10" rx="1" fill="#0692cd"/><path d="M1.5 3.8L8 9l6.5-5.2" stroke="#fff" stroke-width="1.3" fill="none"/></svg>
      </li>
      <li>www.crestlineplumbing.com.au
        <svg viewBox="0 0 16 16" aria-hidden="true"><circle cx="8" cy="8" r="7" fill="#0692cd"/><path d="M1 8h14M8 1v14M3 4.5h10M3 11.5h10" stroke="#fff" stroke-width="0.9" fill="none"/><ellipse cx="8" cy="8" rx="3.2" ry="7" stroke="#fff" stroke-width="0.9" fill="none"/></svg>
      </li>
    </ul>
    <div class="bottom-band"></div>
  </section>

  <section class="card card-back" aria-label="Business card back">
    <div class="back-brand">
      <span class="brand-dot"></span>
      <span class="brand-name">Crestline Plumbing</span>
    </div>
    <div class="licence-row">
      <span class="line"></span>
      <span class="licence">Lic.508264K</span>
      <span class="line"></span>
    </div>
  </section>
</body>
</html>
```